Website for Brisbeck Current Glide

Require a website for a river float in the City of Edmonton. Located on North Saskatchewan River. Will need to be a coded website with incorporated booking system through Fare Harbor software.

Pages include
Home
Pricing
About
FAQ
Contact

Brisbeck Current Glide is an activity based business that will have customers floating down the North Saskatchewan river in Edmonton AB. The site will have all information needed and a full reservation system. The project was launched to provide people in the Edmonton area a favorite summer activity.

Here are similar websites to reference what our business will be doing and what we are looking for.

mellowbendcanoehire.example
pinegulchloopers.example

Target Market(s)

Families, Groups, Individuals, Anyone who wants to explore the river

Industry/Entity Type

Activities based business/ Outdoor recreational/ River Float

Coding

Coded - Design and coding required

Number of Pages Required

5+ page

Colors
0054AA
0677BA
7BADD7
CADEEF
E8F1F8
F0912C
F2A743
F7CA91
FBE8D2
FDF5EE

```html
<!DOCTYPE html>
<html lang="en">
<head>
<meta charset="utf-8">
<title>Brisbeck Current Glide</title>
<link href="https://fonts.googleapis.com/css2?family=Montserrat:wght@400;500;600;700;800&display=swap" rel="stylesheet">
<style>
:root{
  --orange:#e35a2b;
  --orange-soft:#f0912c;
  --navy:#123a6b;
  --navy-deep:#0d2e57;
  --sky:#4dc3e4;
  --light-blue:#cadeef;
  --ink:#1d1d1d;
  --grey:#8a8a8a;
  --white:#ffffff;
  --footer:#1b1b1b;
  --faq-bg:#234d84;
}
*{box-sizing:border-box;margin:0;padding:0}
html,body{width:1200px;height:3423px;overflow:hidden}
body{position:relative;font-family:"Montserrat",sans-serif;color:var(--ink);background:var(--white)}
.abs{position:absolute}
.topbar{left:0;top:0;width:1200px;height:29px;background:var(--orange);color:#fff;font-size:12px;text-align:center;line-height:29px}
.hero{left:0;top:29px;width:1200px;height:566px;background:linear-gradient(180deg,#f4f2ec 0%,#e8c99a 22%,#8a8f7c 45%,#4e6b3f 62%,#2f4a2c 80%,#3e6a2b 100%)}
.brand{left:149px;top:62px;display:flex;align-items:center;gap:8px;font-weight:800;font-size:17px;color:var(--navy);width:200px;line-height:1.1}
.brand-dot{width:30px;height:30px;border-radius:50%;background:var(--sky);flex:none}
.nav a{position:absolute;top:73px;font-size:13px;font-weight:600;color:var(--navy);text-decoration:none}
.nav .btn-contact{left:932px;top:60px;width:110px;height:36px;border-radius:18px;background:var(--navy-deep);color:#fff;line-height:36px;text-align:center;font-weight:500}
.hero-title{left:0;top:298px;width:1200px;text-align:center;color:#fff;font-weight:800;font-size:58px;letter-spacing:.5px}
.hero-sub{left:0;top:364px;width:1200px;text-align:center;color:#fff;font-weight:600;font-size:19px}
.btn{display:block;text-align:center;color:#fff;background:var(--orange);border-radius:24px;font-weight:600;text-decoration:none}
.dots{left:573px;top:518px;display:flex;gap:9px}
.dots span{width:12px;height:12px;border-radius:50%;background:#fff}
.dots span:first-child{background:var(--sky)}
.pricing-bg{left:0;top:595px;width:1200px;height:544px;background:linear-gradient(180deg,#3d6f86 0%,#2a5e78 40%,#5f93a8 100%)}
.section-title{text-align:center;width:1200px;left:0;font-size:36px;font-weight:500;color:#fff}
.price-card{left:121px;top:715px;width:958px;height:424px;background:#fff;border-radius:6px 6px 0 0}
.price-band{left:128px;top:723px;width:943px;height:84px;background:var(--sky);border-radius:4px;color:#fff}
.price-band .name{position:absolute;left:85px;top:24px;font-size:29px;font-weight:500}
.price-band .rule{position:absolute;left:350px;top:44px;width:46px;height:2px;background:#fff;box-shadow:0 5px 0 #fff}
.price-band .amount{position:absolute;left:409px;top:24px;font-size:29px;font-weight:600}
.price-band .outline{position:absolute;left:645px;top:19px;width:167px;height:46px;border:2px solid #fff;border-radius:24px;text-align:center;line-height:42px;font-size:14px;font-weight:500}
.price-desc{left:300px;top:832px;width:600px;text-align:center;font-size:14px;line-height:20px}
.features{left:150px;top:910px;width:900px;height:60px}
.feature{position:absolute;width:150px;margin-left:-75px;text-align:center;font-size:12.5px;color:#555}
.feature svg{display:block;margin:0 auto 6px;width:36px;height:36px}
.group{left:0;top:1068px;width:1200px;text-align:center;font-size:30px;font-weight:600}
.group a{color:var(--navy);text-decoration:none;border-bottom:2px solid var(--navy)}
.note{left:0;top:1115px;width:1200px;text-align:center;font-size:15px}
.note span{border-bottom:1px solid var(--ink)}
.about-photo{left:157px;top:1229px;width:408px;height:326px;border-radius:50% 50% 46% 46%;background:linear-gradient(160deg,#9fb9c2 0%,#5e8fa3 45%,#c94438 70%,#3f6f86 100%)}
.about-arc{left:150px;top:1229px;width:420px;height:420px;border-radius:50%;border:1px solid var(--orange);clip-path:inset(0 0 70% 0)}
.eyebrow{left:607px;top:1243px;font-size:12px;color:var(--orange);display:flex;align-items:center;gap:12px}
.eyebrow i{width:12px;height:12px;border:3px solid var(--sky);border-radius:50%;display:block}
.about-head{left:605px;top:1268px;width:460px;font-size:23px;font-weight:500;line-height:26px;color:#111}
.about-text{left:607px;top:1360px;width:430px;font-size:12.5px;line-height:20px;color:var(--grey)}
.about-text a{color:var(--sky);text-decoration:none}
.faq{left:0;top:1690px;width:1200px;height:546px;background:linear-gradient(180deg,#2b548a 0%,#204a80 60%,#2a5a92 100%)}
.faq-item{position:absolute;border:1px solid rgba(255,255,255,.85);border-radius:6px;color:#fff;font-size:14px;font-weight:600;padding:0 19px;display:flex;align-items:center;justify-content:space-between}
.faq-item.open{display:block;padding:20px 19px}
.faq-item.open p{font-weight:400;font-size:12px;line-height:17px;margin-top:8px}
.chev{width:10px;height:10px;border-right:2px solid #fff;border-bottom:2px solid #fff;transform:rotate(-45deg)}
.chev.down{position:absolute;right:24px;top:20px;transform:rotate(45deg);width:8px;height:8px}
.testi{left:0;top:2236px;width:1200px;height:446px;background:linear-gradient(180deg,#6d6a48 0%,#4d5a3c 50%,#7d6a2a 100%)}
.card{position:absolute;top:2374px;width:272px;height:215px;background:#fff;padding:26px 24px}
.stars{color:#f6b500;font-size:16px;letter-spacing:3px}
.card p{margin-top:12px;font-size:12.5px;line-height:17.5px;color:var(--grey)}
.card b{display:block;margin-top:16px;font-weight:500;font-size:12.5px;color:#222}
.map{left:633px;top:2682px;width:567px;height:361px;background:linear-gradient(160deg,#a9c5f2 0%,#a9c5f2 20%,#dcebd9 30%,#cfe3cc 65%,#eeeeee 100%)}
.contact-head{left:160px;top:2748px;font-size:25px;font-weight:700;color:var(--navy)}
.line-item{position:absolute;display:flex;align-items:center;gap:10px;font-size:15px;color:#333}
.ico{width:24px;height:24px;flex:none}
.social{position:absolute;display:flex;align-items:center;gap:10px;font-size:14px;font-weight:700}
.social .pill{display:flex;align-items:center;gap:5px}
.social .pill i{width:28px;height:28px;border-radius:50%;display:block}
.visit{left:158px;top:2928px;font-size:17px;font-weight:500;color:var(--navy)}
.footer{left:0;top:3043px;width:1200px;height:380px;background:var(--footer);color:#fff}
.f-head{position:absolute;font-size:15px;font-weight:700}
.f-line{position:absolute;display:flex;align-items:center;gap:8px;font-size:15px}
.f-nav a{position:absolute;left:912px;color:#fff;text-decoration:none;font-size:14px}
.subscribe{left:509px;top:3287px;width:287px;height:36px;display:flex;border:1px solid #777;border-radius:4px;overflow:hidden}
.subscribe span{flex:1;font-size:12px;color:#999;padding-left:14px;line-height:34px}
.subscribe b{width:120px;background:var(--orange);text-align:center;line-height:34px;font-size:13px}
.f-rule{left:0;top:3376px;width:1200px;height:1px;background:#3a3a3a}
.copy{left:0;top:3394px;width:1200px;text-align:center;font-size:11px;color:#ccc}
</style>
</head>
<body>

<div class="abs topbar">We provide the lifejacket, paddle, river tube and shuttle service.</div>

<div class="abs hero" role="img" aria-label="Photo of the Edmonton downtown skyline above the river at sunset with green riverbank"></div>
<div class="abs brand"><span class="brand-dot"></span><span>Brisbeck Current Glide</span></div>
<nav class="nav">
  <a style="left:589px">HOME</a>
  <a style="left:674px">PRICING</a>
  <a style="left:773px">ABOUT</a>
  <a style="left:865px">FAQ</a>
  <a class="btn-contact">CONTACT</a>
</nav>
<h1 class="abs hero-title">BRISBECK CURRENT GLIDE</h1>
<p class="abs hero-sub">Float the North Saskatchewan through downtown Edmonton</p>
<a class="abs btn" style="left:518px;top:408px;width:164px;height:45px;line-height:45px;font-size:14px">BOOK NOW</a>
<div class="abs dots"><span></span><span></span><span></span></div>

<section>
  <div class="abs pricing-bg" role="img" aria-label="Photo of people relaxing on inflatable tubes on the river"></div>
  <h2 class="abs section-title" style="top:640px">°• Pricing</h2>
  <div class="abs price-card"></div>
  <div class="abs price-band">
    <span class="name">Tube and Shuttle</span><span class="rule"></span>
    <span class="amount">$30/person</span><span class="outline">BOOK NOW</span>
  </div>
  <p class="abs price-desc">We keep our pricing simple and include everything you need: Premium com fort float tube with backrest and cup holder</p>
  <div class="abs features">
    <div class="feature" style="left:59px"><svg viewBox="0 0 36 36" fill="none" stroke="#1f4f8a" stroke-width="1.5"><path d="M11 5h5v5h4V5h5l4 6v20H7V11z"/><path d="M7 20h22M7 25h22"/></svg>Lifejacket</div>
    <div class="feature" style="left:154px"><svg viewBox="0 0 36 36" fill="none" stroke="#1f4f8a" stroke-width="1.5"><ellipse cx="13" cy="10" rx="4" ry="7"/><path d="M13 17v16"/><ellipse cx="23" cy="10" rx="4" ry="7"/><path d="M23 17v16"/></svg>Paddle</div>
    <div class="feature" style="left:298px"><svg viewBox="0 0 36 36" fill="none" stroke="#1f4f8a" stroke-width="1.5"><rect x="4" y="11" width="26" height="16" rx="2" transform="rotate(-10 17 19)"/><path d="M9 20h10M9 24h6"/></svg>Round trip shuttle service</div>
    <div class="feature" style="left:463px"><svg viewBox="0 0 36 36" fill="none" stroke="#1f4f8a" stroke-width="1.5"><path d="M6 22a12 12 0 0 1 24 0z"/><circle cx="25" cy="26" r="6"/><path d="M22 26l2 2 4-4"/></svg>Safety training</div>
    <div class="feature" style="left:600px"><svg viewBox="0 0 36 36" fill="none" stroke="#1f4f8a" stroke-width="1.5"><circle cx="9" cy="11" r="4"/><circle cx="18" cy="9" r="4"/><circle cx="27" cy="11" r="4"/><path d="M2 26c0-6 14-6 14 0M11 24c0-7 14-7 14 0M20 26c0-6 14-6 14 0"/></svg>Staff assistance</div>
    <div class="feature" style="left:715px"><svg viewBox="0 0 36 36"><path d="M18 33s-10-11-10-18a10 10 0 0 1 20 0c0 7-10 18-10 18z" fill="#1f4f8a"/><circle cx="18" cy="15" r="6" fill="#fff"/><text x="18" y="19" text-anchor="middle" font-size="9" font-weight="700" fill="#1f4f8a" font-family="Montserrat,sans-serif">P</text></svg>Parking</div>
    <div class="feature" style="left:827px"><svg viewBox="0 0 36 36" fill="none" stroke="#1f4f8a" stroke-width="1.5"><path d="M8 30l6-14 8 8z"/><path d="M20 8v4M26 12l-3 3M30 20h-4M24 4l1 2M30 8l-2 1"/></svg>Unlimited Fun!</div>
  </div>
  <a class="abs btn" style="left:537px;top:1006px;width:125px;height:39px;line-height:39px;font-size:13px">BOOK NOW</a>
  <p class="abs group">Group of 10 or more? <a>Contact us</a></p>
  <p class="abs note"><span>*does not include taxes or fees</span></p>
</section>

<section>
  <div class="abs about-arc"></div>
  <div class="abs about-photo" role="img" aria-label="Photo of a family on a red towable tube splashing across a lake"></div>
  <div class="abs eyebrow">About Us <i></i></div>
  <h2 class="abs about-head">Float the North Saskatchewan through downtown Edmonton<br>Edmonton’s Best Summer Activity</h2>
  <p class="abs about-text">We provide the lifejacket, paddle, river tube and shuttle service. You just have to show up. Brisbeck Current Glide was launched to provide people in the Edmonton area a favorite summeractivity. Nothing is better on a hot summer day, than spending it on the river and seeing Edmonton from a new perspective. Our home base and meeting spot is at Pier Nine Landing <a>(Map Link)</a>, by the Glasshouse Gardens. This is where you will check in, and board the shuttle. The shuttle will take all floaters up river to Willow Flats Boat Launch, where your tube will be waiting. Once on the river, you can sit back, relax, explore and enjoy the</p>
  <a class="abs btn" style="left:607px;top:1577px;width:125px;height:37px;line-height:37px;font-size:13px;background:var(--navy-deep);font-weight:500">BOOK NOW</a>
</section>

<section>
  <div class="abs faq" role="img" aria-label="Blue-tinted photo of floaters on river tubes"></div>
  <h2 class="abs section-title" style="top:1758px;font-weight:600">FAQ°•</h2>
  <div class="faq-item open" style="left:158px;top:1847px;width:441px;height:116px">How do I reserve my float?<span class="chev down"></span><p>We highly recommend booking online, as we do sell out. <u>BOOK NOW</u> Floats can also be reserved on-site at Pier Nine Landing, on a first come first serve basis.</p></div>
  <div class="faq-item" style="left:158px;top:1971px;width:441px;height:46px">Where should I park?<span class="chev"></span></div>
  <div class="faq-item" style="left:158px;top:2025px;width:441px;height:48px">What time should I arrive?<span class="chev"></span></div>
  <div class="faq-item" style="left:611px;top:1847px;width:431px;height:46px">What safety information should I know?<span class="chev"></span></div>
  <div class="faq-item" style="left:611px;top:1903px;width:431px;height:47px">What is included?<span class="chev"></span></div>
  <div class="faq-item" style="left:611px;top:1960px;width:431px;height:47px">What should I bring?<span class="chev"></span></div>
  <div class="faq-item" style="left:611px;top:2017px;width:431px;height:48px">Where are you located?<span class="chev"></span></div>
  <a class="abs btn" style="left:544px;top:2104px;width:113px;height:35px;line-height:35px;font-size:13px">SEE ALL</a>
</section>

<section>
  <div class="abs testi" role="img" aria-label="Photo of a group floating on yellow tubes down the river"></div>
  <h2 class="abs section-title" style="top:2296px">Testimonials°•</h2>
  <div class="card" style="left:158px"><div class="stars">★★★★★</div><p>Sed ut perspiciatis unde omnis iste natus error sit voluptatem accusan-tium doloremque laudantium, totam rem aperiam, eaque ipsa quae ab illo inventore veritatis et quasi</p><b>- Lorem ipsum</b></div>
  <div class="card" style="left:464px"><div class="stars">★★★★★</div><p>Sed ut perspiciatis unde omnis iste natus error sit voluptatem accusan-tium doloremque laudantium, totam rem aperiam, eaque ipsa quae ab illo inventore veritatis et quasi</p><b>- Lorem ipsum</b></div>
  <div class="card" style="left:769px"><div class="stars">★★★★★</div><p>Sed ut perspiciatis unde omnis iste natus error sit voluptatem accusan-tium doloremque laudantium, totam rem aperiam, eaque ipsa quae ab illo inventore veritatis et quasi</p><b>- Lorem ipsum</b></div>
</section>

<section>
  <h2 class="abs contact-head">We’d love to hear from you!</h2>
  <div class="line-item" style="left:158px;top:2795px"><svg class="ico" viewBox="0 0 24 24" fill="none" stroke="#1f3f6b" stroke-width="1.6"><circle cx="12" cy="12" r="10.5"/><path d="M8.5 7l2 2.5-1 1.5a6 6 0 0 0 3.5 3.5l1.5-1 2.5 2-1.2 1.5c-4 0-8.3-4.3-8.3-8.3z"/></svg>555-010-2244</div>
  <div class="line-item" style="left:158px;top:2827px"><svg class="ico" viewBox="0 0 24 24" fill="none" stroke="#1f3f6b" stroke-width="1.6"><circle cx="12" cy="12" r="10.5"/><rect x="7" y="8.5" width="10" height="7"/><path d="M7 8.5l5 4 5-4"/></svg>hello@brisbeckglide.example</div>
  <div class="social" style="left:158px;top:2874px">
    <span class="pill"><i style="background:var(--navy)"></i>FaceSpot</span>
    <span class="pill"><i style="background:var(--navy)"></i>PhotoLane</span>
    <span class="pill"><i style="background:#34e0a1"></i>TrailNotes</span>
  </div>
  <p class="abs visit">Come visit us on float days at Pier Nine Landing</p>
  <div class="line-item" style="left:158px;top:2960px"><svg class="ico" viewBox="0 0 24 24" fill="none" stroke="#1f3f6b" stroke-width="1.6"><circle cx="12" cy="12" r="10.5"/><path d="M12 18s-4-4-4-7a4 4 0 0 1 8 0c0 3-4 7-4 7z"/><circle cx="12" cy="11" r="1.3"/></svg>4410 Alder Bend Rd, Edmonton, AB</div>
  <div class="abs map" role="img" aria-label="Street map showing the river, the landing and the meeting point pin"></div>
</section>

<footer>
  <div class="abs footer"></div>
  <div class="f-head" style="left:158px;top:3117px">BRISBECK CURRENT GLIDE</div>
  <div class="f-line" style="left:158px;top:3157px"><svg class="ico" viewBox="0 0 24 24" fill="none" stroke="#fff" stroke-width="1.6"><circle cx="12" cy="12" r="10.5"/><rect x="7" y="8.5" width="10" height="7"/><path d="M7 8.5l5 4 5-4"/></svg>hello@brisbeckglide.example</div>
  <div class="f-line" style="left:158px;top:3193px"><svg class="ico" viewBox="0 0 24 24" fill="none" stroke="#fff" stroke-width="1.6"><circle cx="12" cy="12" r="10.5"/><path d="M12 18s-4-4-4-7a4 4 0 0 1 8 0c0 3-4 7-4 7z"/><circle cx="12" cy="11" r="1.3"/></svg>4410 Alder Bend Rd, Edmonton, AB</div>
  <div class="social" style="left:158px;top:3237px;color:#fff">
    <span class="pill"><i style="background:#fff"></i>FaceSpot</span>
    <span class="pill"><i style="background:#fff"></i>PhotoLane</span>
    <span class="pill"><i style="background:#34e0a1"></i>TrailNotes</span>
  </div>
  <div class="f-head" style="left:0;width:1310px;text-align:center;top:3113px">FLOATING 7 DAYS A WEEK</div>
  <div class="abs" style="left:555px;top:3170px;width:200px;display:flex;flex-direction:column;align-items:center;gap:8px;color:#fff;font-weight:800;font-size:16px">
    <span style="width:40px;height:40px;border-radius:50%;background:var(--sky);display:block"></span>Brisbeck Current Glide
  </div>
  <p class="abs" style="left:0;width:1310px;text-align:center;top:3253px;color:#fff;font-size:14px">Sign up for our newsletter</p>
  <div class="abs subscribe"><span>Enter email id</span><b>SUBSCRIBE</b></div>
  <div class="f-head" style="left:910px;top:3113px">NAVIGATION</div>
  <nav class="f-nav">
    <a style="top:3148px">HOME</a><a style="top:3179px">PRICING</a><a style="top:3210px">ABOUT</a><a style="top:3240px">FAQ</a><a style="top:3272px">CONTACT</a>
  </nav>
  <div class="abs f-rule"></div>
  <p class="abs copy">©Copyright 2022 | All rightsreserved.</p>
</footer>

</body>
</html>
```